New business logo / Business Card Design

My company provides Interim Management and consultancy, for Facilities Services. Covers any aspect of facilities management, including M&E, helpdesk, asset management, supplier relationships, catering, cleaning etc. Company provides innovative solutions to exceed client needs, drawing on years of experience. Initial thoughts on logo are attached below. Fits with RAG status on projects, red, amber and green, with logo design colours around moving services from amber to green.

Target Market(s)

Facilities Management clients and service providers

Industry/Entity Type

Business

Contact Information for Business Card

Company Name = k7Rventures Ltd My name on card = Derek Whitcombe, Director Mobile = 07516309842 Email = Derek@k7rventuresltd.co.uk Twitter = @k7Rventures Ltd

Font styles to use
Sans Serif

Colors
f37122
00a990

Requirements
Must have
• Logo to be evident, with some background image in reference to Facilities Management

```html
<!DOCTYPE html>
<html lang="en">
<head>
<meta charset="utf-8">
<title>k7r ventures Ltd – Business Card</title>
<link href="https://fonts.googleapis.com/css2?family=Questrial&family=Lato:wght@400;700&display=swap" rel="stylesheet">
<style>
  :root {
    --stage: #ecebe8;
    --card: #ffffff;
    --brand-green: #006a12;
    --brand-orange: #f37122;
    --ring-grey: #9a9a9a;
    --ink: #1c1c1c;
    --rule: #8a8a8a;
  }
  * { margin: 0; padding: 0; box-sizing: border-box; }
  html, body { width: 1200px; height: 900px; overflow: hidden; }
  body { background: var(--stage); position: relative; font-family: "Lato", sans-serif; color: var(--ink); }

  .card { position: absolute; background: var(--card); box-shadow: 0 4px 14px rgba(0,0,0,0.18); overflow: hidden; }

  /* Front */
  .card-front { left: 78px; top: 35px; width: 587px; height: 363px; }
  .side-band { position: absolute; left: 29px; top: 0; width: 126px; height: 100%; background: var(--brand-green); }
  .front-mark { position: absolute; left: 27px; top: 25px; width: 130px; height: 130px; }
  .company-name { font-family: "Questrial", sans-serif; font-weight: 400; color: var(--ink); white-space: nowrap; }
  .card-front .company-name { position: absolute; left: 174px; top: 70px; font-size: 33px; }
  .holder-name { position: absolute; left: 174px; top: 190px; font-size: 22px; font-weight: 700; color: var(--brand-green); }
  .holder-role { position: absolute; left: 174px; top: 219px; font-size: 16px; }
  .divider { position: absolute; left: 174px; top: 248px; width: 191px; height: 1px; background: var(--rule); }
  .contact-list { position: absolute; left: 0; top: 262px; list-style: none; }
  .contact-item { position: relative; height: 24.5px; padding-left: 174px; font-size: 15.5px; line-height: 24px; }
  .contact-icon { position: absolute; left: 136px; top: 6px; width: 12px; height: 12px; }

  /* Back */
  .card-back { left: 388px; top: 505px; width: 567px; height: 352px; }
  .back-mark { position: absolute; left: 212px; top: 92px; width: 126px; height: 126px; }
  .card-back .company-name { position: absolute; left: 0; width: 100%; top: 224px; text-align: center; font-size: 29px; }
</style>
</head>
<body>

<section class="card card-front" aria-label="Business card front">
  <div class="side-band"></div>
  <svg class="front-mark" viewBox="0 0 130 130" aria-hidden="true">
    <circle cx="65" cy="65" r="62" fill="#ffffff"/>
    <circle cx="65" cy="65" r="60" fill="none" stroke="var(--ring-grey)" stroke-width="4"/>
    <circle cx="65" cy="65" r="54" fill="var(--brand-orange)"/>
  </svg>
  <h1 class="company-name">k7r ventures Ltd</h1>

  <p class="holder-name">Derek Whitcombe</p>
  <p class="holder-role">Director</p>
  <div class="divider"></div>

  <ul class="contact-list">
    <li class="contact-item">
      <svg class="contact-icon" viewBox="0 0 12 12" aria-hidden="true"><path d="M2.4 0.8 L4.2 3 L3.2 4.3 C3.9 5.8 5.2 7.1 6.7 7.8 L8 6.8 L10.2 8.6 L9.3 10.6 C5 10.4 1.6 7 1.4 2.7 Z" fill="#ffffff"/></svg>
      07516309842
    </li>
    <li class="contact-item">
      <svg class="contact-icon" viewBox="0 0 12 12" aria-hidden="true"><rect x="0.8" y="2.5" width="10.4" height="7.5" fill="none" stroke="#ffffff" stroke-width="1.2"/><path d="M0.8 2.5 L6 6.8 L11.2 2.5" fill="none" stroke="#ffffff" stroke-width="1.2"/></svg>
      Derek@k7rventuresltd.co.uk
    </li>
    <li class="contact-item">
      <svg class="contact-icon" viewBox="0 0 12 12" aria-hidden="true"><circle cx="6" cy="6" r="5" fill="#ffffff"/></svg>
      @k7Rventures Ltd
    </li>
  </ul>
</section>

<section class="card card-back" aria-label="Business card back">
  <svg class="back-mark" viewBox="0 0 126 126" aria-hidden="true">
    <circle cx="63" cy="63" r="60" fill="none" stroke="var(--ring-grey)" stroke-width="4"/>
    <circle cx="63" cy="63" r="54" fill="var(--brand-orange)"/>
  </svg>
  <h2 class="company-name">k7r ventures Ltd</h2>
</section>

</body>
</html>
```